Voltarey - Flyer design

Description -
Motorhome and Caravan EWOFs
Recreational Vehicles (such as caravans, motorhomes, RVs, Boats etc) and Relocatable buildings that can be connected to an electricity supply must be regularly checked for electrical safety. An EWOF needs to be issued every 4 years.
Pre-purchase house inspections
A pre-purchase electrical inspection prior to buying a home can be used to identify any dangerous and unsafe electrical parts of the installation that may be costly to repair once the property has been purchased. Giving you peace of mind when buying your new home.
High risk Electrical inspections
All Prescribed Electrical Work that falls under the High Risk category must be inspected by a Registered Electrical Inspector and have a Record of Inspection certificate issued.
Electric Vehicle Chargers
Any electrical vehicle charger that can be accessed by the public (ie in a non-domestic situation) must be periodically inspected and certified every 12 months.
General Electrical Services
Domestic and commercial - We do new builds, Renovations, Maintenance and more!
Dean Fowler - Electrician and Electrical Inspector
Ph - 0227839152
Dean@voltarey.co.nz
Auckland
------
I also want there to be a few symbols similar to the files I have attached.
The main areas that I am hoping to find work is with caravans/motohomes and EV car chargers so these symbols are quite important.
Thanks so much

```html
<!DOCTYPE html>
<html lang="en">
<head>
<meta charset="utf-8">
<title>Voltarey – Electrical Inspections Flyer</title>
<link href="https://fonts.googleapis.com/css2?family=Montserrat:wght@500;600;700;800;900&family=Open+Sans:wght@400;600;700&display=swap" rel="stylesheet">
<style>
  :root{
    --green:#6cbf3a;
    --green-dark:#4f9a25;
    --ink:#1f2a30;
    --body:#4a5358;
    --muted:#7b8489;
    --paper:#ffffff;
    --stage:#e9ecee;
    --sky-top:#7fa7c9;
    --sky-low:#c9d9e6;
    --hill:#5e7f43;
  }
  *{box-sizing:border-box;margin:0;padding:0}
  html,body{width:759px;height:1200px;overflow:hidden}
  body{background:var(--stage);font-family:"Open Sans",Arial,sans-serif;color:var(--body)}
  .flyer{position:absolute;left:29px;top:25px;width:700px;height:1150px;background:var(--paper);overflow:hidden;box-shadow:0 2px 10px rgba(0,0,0,.12)}
  .hero{position:absolute;left:0;top:0;width:700px;height:470px;
    background:linear-gradient(180deg,var(--sky-top) 0%,var(--sky-low) 38%,#9fb68a 55%,var(--hill) 72%,#cfd5d8 86%,#aab2b6 100%)}
  .hero-icons{position:absolute;right:30px;top:40px;width:230px;height:170px;border-radius:8px;
    background:linear-gradient(135deg,rgba(255,255,255,.18),rgba(255,255,255,.05))}
  .hero-title{position:absolute;left:32px;top:92px;font-family:"Montserrat",Arial,sans-serif;font-weight:800;
    font-size:52px;line-height:1.06;color:#fff;letter-spacing:-.5px;text-shadow:0 2px 6px rgba(0,0,0,.25)}
  .specialty{position:absolute;left:0;top:462px;width:440px;height:124px}
  .specialty svg{position:absolute;inset:0}
  .specialty h2{position:relative;padding:16px 0 0 30px;font-family:"Montserrat",Arial,sans-serif;font-weight:800;
    font-size:25px;line-height:1.18;color:#fff}
  .photo{position:absolute;border:4px solid #fff;box-shadow:0 1px 4px rgba(0,0,0,.15)}
  .photo-charger{left:440px;top:478px;width:248px;height:158px;background:linear-gradient(135deg,#b9d6a3,#5d8d4a 60%,#2f3d36)}
  .photo-caravan{left:440px;top:642px;width:248px;height:196px;background:linear-gradient(180deg,#b8d3ea 0%,#dfe8ee 45%,#f2f2f0 60%,#8aa36f 100%)}
  .line-icons{position:absolute;left:450px;top:860px;width:230px;height:150px;border-radius:6px;background:linear-gradient(180deg,#f4f6f5,#eef1ef)}
  .services{position:absolute;left:26px;top:604px;width:400px;list-style:none}
  .service{position:relative;padding-left:30px;margin-bottom:13px}
  .service svg{position:absolute;left:0;top:1px;width:20px;height:20px}
  .service h3{font-family:"Montserrat",Arial,sans-serif;font-weight:700;font-size:15px;color:var(--ink);line-height:1.3;margin-bottom:3px}
  .service p{font-size:11px;line-height:1.45;color:var(--body)}
  .footer{position:absolute;left:0;top:1034px;width:700px;height:100px;border-top:1px solid #dde2e4}
  .brand{position:absolute;left:26px;top:28px;display:flex;align-items:center;gap:8px}
  .brand-mark{width:22px;height:22px;background:var(--green)}
  .brand-name{font-family:"Montserrat",Arial,sans-serif;font-weight:700;font-size:26px;color:var(--ink)}
  .divider{position:absolute;left:225px;top:20px;width:1px;height:60px;background:#cfd5d8}
  .person{position:absolute;left:245px;top:20px}
  .person-name{font-family:"Montserrat",Arial,sans-serif;font-weight:700;font-size:16px;color:var(--ink)}
  .person-role{font-size:10.5px;color:var(--muted);margin-top:1px}
  .person-phone{font-family:"Montserrat",Arial,sans-serif;font-weight:600;font-size:13px;color:var(--ink);margin-top:8px}
  .contacts{position:absolute;left:470px;top:18px;list-style:none}
  .contacts li{display:flex;align-items:center;gap:8px;font-size:11.5px;color:var(--body);height:22px}
  .contacts svg{width:14px;height:14px}
  .base-strip{position:absolute;left:0;bottom:0;width:700px;height:16px;background:var(--green)}
</style>
</head>
<body>
<main class="flyer">
  <section class="hero" role="img" aria-label="Photo of motorhomes and caravans parked in a grassy valley with mountains behind">
    <div class="hero-icons" role="img" aria-label="Line illustration of an electrician with an EV charger"></div>
  </section>
  <h1 class="hero-title">Electrical<br>Inspections<br>You Can Trust</h1>

  <div class="specialty">
    <svg viewBox="0 0 440 124" preserveAspectRatio="none" aria-hidden="true">
      <polygon points="0,0 440,0 400,124 0,124" fill="#6cbf3a"/>
    </svg>
    <h2>Specializing in<br>Motorhomes, Caravans,<br>and EV Chargers</h2>
  </div>

  <div class="photo photo-charger" role="img" aria-label="Photo of an electric vehicle charging plug connected to a car"></div>
  <div class="photo photo-caravan" role="img" aria-label="Photo of a white caravan parked on grass"></div>
  <div class="line-icons" role="img" aria-label="Line icons of a caravan and an EV charging station"></div>

  <ul class="services">
    <li class="service">
      <svg viewBox="0 0 20 20" aria-hidden="true"><circle cx="10" cy="10" r="10" fill="#6cbf3a"/><path d="M5.5 10.3l3 3 6-6.2" stroke="#fff" stroke-width="2" fill="none" stroke-linecap="round" stroke-linejoin="round"/></svg>
      <h3>Motorhome &amp; Caravan EWOFs</h3>
      <p>Recreational Vehicles (such as caravans, motorhomes, RVs, Boats etc) and Relocatable buildings that can be connected to an electricity supply must be regularly checked for electrical safety. An EWOF needs to be issued every 4 years.</p>
    </li>
    <li class="service">
      <svg viewBox="0 0 20 20" aria-hidden="true"><circle cx="10" cy="10" r="10" fill="#6cbf3a"/><path d="M5.5 10.3l3 3 6-6.2" stroke="#fff" stroke-width="2" fill="none" stroke-linecap="round" stroke-linejoin="round"/></svg>
      <h3>Pre-purchase House Inspections</h3>
      <p>A pre-purchase electrical inspection prior to buying a home can be used to identify any dangerous and unsafe electrical parts of the installation that may be costly to repair once the property has been purchased. Giving you peace of mind when buying your new home.</p>
    </li>
    <li class="service">
      <svg viewBox="0 0 20 20" aria-hidden="true"><circle cx="10" cy="10" r="10" fill="#6cbf3a"/><path d="M5.5 10.3l3 3 6-6.2" stroke="#fff" stroke-width="2" fill="none" stroke-linecap="round" stroke-linejoin="round"/></svg>
      <h3>High Risk Electrical Inspections</h3>
      <p>All Prescribed Electrical Work that falls under the High Risk category must be inspected by a Registered Electrical Inspector and have a Record of Inspection certificate issued.</p>
    </li>
    <li class="service">
      <svg viewBox="0 0 20 20" aria-hidden="true"><circle cx="10" cy="10" r="10" fill="#6cbf3a"/><path d="M5.5 10.3l3 3 6-6.2" stroke="#fff" stroke-width="2" fill="none" stroke-linecap="round" stroke-linejoin="round"/></svg>
      <h3>Electric Vehicle Chargers</h3>
      <p>Any electrical vehicle charger that can be accessed by the public (ie in a non-domestic situation) must be periodically inspected and certified every 12 months.</p>
    </li>
    <li class="service">
      <svg viewBox="0 0 20 20" aria-hidden="true"><circle cx="10" cy="10" r="10" fill="#6cbf3a"/><path d="M5.5 10.3l3 3 6-6.2" stroke="#fff" stroke-width="2" fill="none" stroke-linecap="round" stroke-linejoin="round"/></svg>
      <h3>General Electrical Services</h3>
      <p>Domestic and commercial - We do new builds, Renovations, Maintenance and more!</p>
    </li>
  </ul>

  <footer class="footer">
    <div class="brand"><span class="brand-mark"></span><span class="brand-name">Voltarey</span></div>
    <span class="divider"></span>
    <div class="person">
      <div class="person-name">Dean Fowler</div>
      <div class="person-role">Electrician &amp; Electrical<br>Inspector</div>
      <div class="person-phone">022 783 9152</div>
    </div>
    <ul class="contacts">
      <li><svg viewBox="0 0 14 14" aria-hidden="true"><rect x="1" y="3" width="12" height="8" rx="1" fill="none" stroke="#6cbf3a" stroke-width="1.3"/><path d="M1.5 3.5L7 8l5.5-4.5" fill="none" stroke="#6cbf3a" stroke-width="1.3"/></svg>Dean@voltarey.co.nz</li>
      <li><svg viewBox="0 0 14 14" aria-hidden="true"><circle cx="7" cy="7" r="5.6" fill="none" stroke="#6cbf3a" stroke-width="1.3"/><ellipse cx="7" cy="7" rx="2.4" ry="5.6" fill="none" stroke="#6cbf3a" stroke-width="1.1"/><path d="M1.4 7h11.2" stroke="#6cbf3a" stroke-width="1.1"/></svg>www.voltarey.co.nz</li>
      <li><svg viewBox="0 0 14 14" aria-hidden="true"><path d="M7 13s-4.2-4.6-4.2-7.6a4.2 4.2 0 018.4 0C11.2 8.4 7 13 7 13z" fill="none" stroke="#6cbf3a" stroke-width="1.3"/><circle cx="7" cy="5.4" r="1.5" fill="#6cbf3a"/></svg>Auckland, NZ</li>
    </ul>
  </footer>
  <div class="base-strip"></div>
</main>
</body>
</html>
```